Financial Planning Business needs a business card design

We need a business card design that is for a new financial planning business based in Australia. We provide financial planning advice such as retirement planning, wealth creation, asset protection.

Attached is the logo design. On the front side of the business card needs to incorporate the following:
- adviser name
- adviser title (ie Managing Director)
- address
- phone number
- email
- website address

Ideally it should also have the business name and logo

On the back of the card I would like this to be black in colour with the business name and logo

I have been advised the font is "Cinzel" (regular and bold)

Industry/Entity Type

Financial

Requirements
Must have
• Logo and business name

Format to have as follows:
Ben xxxxxxxx
Managing Director / Senior Financial Adviser
address
phone email
website

```html
<!DOCTYPE html>
<html lang="en">
<head>
<meta charset="utf-8">
<title>Harbourline Wealth Planning – Business Card</title>
<link href="https://fonts.googleapis.com/css2?family=Cinzel:wght@400;700&family=Open+Sans:wght@400;700&display=swap" rel="stylesheet">
<style>
  :root {
    --page-bg: #e9e9e7;
    --card-white: #ffffff;
    --card-dark: #333333;
    --brand-blue: #2a9ad6;
    --brand-grey: #8a8a8a;
    --text-light: #ffffff;
    --text-soft: #e4e4e4;
    --shadow: rgba(0, 0, 0, 0.18);
  }
  * { box-sizing: border-box; margin: 0; padding: 0; }
  html, body {
    width: 1200px; height: 720px; overflow: hidden;
    background: var(--page-bg);
    font-family: "Open Sans", Arial, sans-serif;
  }
  .stage {
    position: relative; width: 1200px; height: 720px;
    display: flex; align-items: center; justify-content: center; gap: 40px;
  }
  .card {
    position: relative; width: 540px; height: 308px;
    overflow: hidden;
    box-shadow: 0 6px 18px var(--shadow);
  }
  .card--front { background: var(--card-white); }
  .card--back { background: var(--card-dark); }

  .front-swoosh { position: absolute; inset: 0; }

  .brand {
    position: absolute; display: flex; align-items: center; gap: 16px;
  }
  .brand-square { background: var(--brand-grey); flex: none; }
  .brand-name {
    font-family: "Cinzel", Georgia, serif; font-weight: 700;
    text-transform: uppercase; line-height: 1.05; white-space: nowrap;
  }
  .card--front .brand { left: 70px; top: 36px; }
  .card--front .brand-square { width: 46px; height: 46px; }
  .card--front .brand-name { color: var(--brand-blue); font-size: 34px; }
  .card--front .brand-name small { display: block; font-size: 19px; letter-spacing: 1px; }

  .contact {
    position: absolute; left: 150px; top: 186px;
    display: flex; gap: 14px; color: var(--text-light);
  }
  .person { text-align: right; padding-top: 20px; }
  .person-name { font-weight: 700; font-size: 16px; line-height: 1.2; }
  .person-title { font-size: 12px; color: var(--text-soft); margin-bottom: 4px; }
  .person-address { font-size: 12px; line-height: 1.35; color: var(--text-soft); }

  .contact-list { list-style: none; font-size: 12.5px; }
  .contact-list li { display: flex; align-items: center; gap: 7px; height: 19px; white-space: nowrap; }
  .contact-icon { width: 13px; height: 13px; flex: none; }

  .card--back .brand {
    left: 50%; top: 92px; transform: translateX(-50%);
    flex-direction: column; gap: 14px; text-align: center;
  }
  .card--back .brand-square { width: 44px; height: 44px; background: var(--text-light); }
  .card--back .brand-name { color: var(--text-light); font-size: 26px; letter-spacing: 1px; }
  .back-web {
    position: absolute; left: 0; right: 0; bottom: 38px; text-align: center;
    color: var(--text-light); font-size: 15px; letter-spacing: 1.5px;
  }
</style>
</head>
<body>
<main class="stage">

  <section class="card card--front" aria-label="Card front">
    <svg class="front-swoosh" viewBox="0 0 540 308" width="540" height="308" aria-hidden="true">
      <path d="M0 210 C 180 200 380 168 540 132 L540 308 L0 308 Z" fill="var(--card-dark)"/>
      <path d="M0 203 C 180 193 380 161 540 125" fill="none" stroke="var(--brand-blue)" stroke-width="4"/>
    </svg>

    <div class="brand">
      <span class="brand-square"></span>
      <p class="brand-name">Harbourline<small>Wealth Planning</small></p>
    </div>

    <div class="contact">
      <div class="person">
        <p class="person-name">Your Name</p>
        <p class="person-title">Title</p>
        <p class="person-address">Street Name, City Name<br>Zip Code - 000000</p>
      </div>
      <ul class="contact-list">
        <li>
          <svg class="contact-icon" viewBox="0 0 16 16" aria-hidden="true"><circle cx="8" cy="8" r="8" fill="#fff"/><path d="M5 4.5 L6.8 4.5 L7.3 6.6 L6.3 7.4 Q7.2 9.2 8.8 9.9 L9.6 8.9 L11.5 9.4 L11.5 11.2 Q7 11.5 4.8 6.4 Z" fill="#333"/></svg>
          012-345-6789
        </li>
        <li>
          <svg class="contact-icon" viewBox="0 0 16 16" aria-hidden="true"><rect x="4.5" y="1" width="7" height="14" rx="1.5" fill="#fff"/><rect x="5.8" y="3" width="4.4" height="8" fill="#333"/></svg>
          012-345-6789
        </li>
        <li>
          <svg class="contact-icon" viewBox="0 0 16 16" aria-hidden="true"><circle cx="8" cy="8" r="8" fill="#fff"/><rect x="3.5" y="5" width="9" height="6" fill="#333"/><path d="M3.5 5 L8 8.5 L12.5 5" fill="none" stroke="#fff" stroke-width="0.9"/></svg>
          info@harbourlinewealth.com
        </li>
        <li>
          <svg class="contact-icon" viewBox="0 0 16 16" aria-hidden="true"><circle cx="8" cy="8" r="7.5" fill="#fff"/><g fill="none" stroke="#333" stroke-width="0.9"><circle cx="8" cy="8" r="5"/><ellipse cx="8" cy="8" rx="2.2" ry="5"/><path d="M3 8 H13"/></g></svg>
          www.harbourlinewealth.com
        </li>
      </ul>
    </div>
  </section>

  <section class="card card--back" aria-label="Card back">
    <div class="brand">
      <span class="brand-square"></span>
      <p class="brand-name">Harbourline<br>Wealth Planning</p>
    </div>
    <p class="back-web">www.harbourlinewealth.com</p>
  </section>

</main>
</body>
</html>
```